QPVT registered provider offering Supports for clients

We need a flyer/brochure that we can physically hand out and also one we can send out to our customers.

Small enough for people to hold in their hands, maybe A4/A5 size.

We are a small start-up company that needs to get our services known and out there.

This is our website - https://lumenfieldhub.com.au/

Thank you

```html
<!DOCTYPE html>
<html lang="en">
<head>
<meta charset="utf-8">
<title>Lumenfield Hub – Flyer</title>
<link rel="stylesheet" href="https://fonts.googleapis.com/css2?family=Barlow:wght@400;600;700&family=Barlow+Condensed:wght@500;600&family=Passion+One:wght@700&display=swap">
<style>
  :root{
    --purple:#6a2f9e;
    --purple-dark:#5a2590;
    --purple-light:#8a5cc0;
    --lavender:#c9b6e6;
    --green:#6dbb3c;
    --green-dark:#3e8a2a;
    --ink:#2b2b2b;
    --paper:#ffffff;
    --backdrop:#cfc1b6;
  }
  *{box-sizing:border-box;margin:0;padding:0}
  html,body{width:1200px;height:900px;overflow:hidden}
  body{background:var(--backdrop);font-family:"Barlow",sans-serif;position:relative}
  .flyer{position:absolute;left:296px;top:20px;width:608px;height:860px;background:var(--paper);
    box-shadow:0 10px 30px rgba(0,0,0,.18);display:flex;overflow:hidden}
  .flyer__main{width:320px;display:flex;flex-direction:column;position:relative}
  .flyer__side{width:288px;background:linear-gradient(180deg,var(--purple-light) 0%,var(--purple) 35%,var(--purple-light) 70%,var(--green) 100%);
    position:relative;color:#fff}

  .brand{height:96px;display:flex;align-items:center;justify-content:center;gap:8px}
  .brand__dot{width:14px;height:14px;border-radius:50%;background:var(--green)}
  .brand__name{font-weight:700;font-size:24px;color:var(--purple)}

  .hero{height:250px;background:radial-gradient(circle at 72% 38%,#f7d6a0 0%,#d98a4a 18%,#7a3d30 48%,#2a1614 100%)}

  .section-title{margin-top:12px;height:26px;background:linear-gradient(90deg,var(--purple) 0%,var(--purple-light) 45%,var(--lavender) 100%);
    font-family:"Barlow Condensed",sans-serif;font-weight:500;font-size:20px;color:#fff;padding-left:26px;line-height:26px;letter-spacing:.3px}
  .section-body{padding:8px 22px 0 26px;font-size:11.4px;line-height:1.38;color:var(--ink);text-align:justify}

  .services{list-style:none;padding:6px 22px 0 24px}
  .services li{display:flex;align-items:center;gap:6px;font-weight:700;font-size:13px;line-height:17.5px;color:var(--ink)}
  .services svg{width:11px;height:11px;flex:none}

  .phone{position:absolute;left:0;right:0;bottom:0;height:82px;background:var(--purple);color:#fff;display:flex;align-items:center;gap:8px;padding-left:30px}
  .phone svg{width:24px;height:30px}
  .phone__number{font-family:"Barlow Condensed",sans-serif;font-weight:600;font-size:44px;letter-spacing:1px}

  .site{position:absolute;top:34px;left:36px;border:1.5px solid #fff;border-radius:12px;padding:2px 10px;font-size:10.5px;display:flex;align-items:center;gap:5px}
  .site::before{content:"";width:5px;height:5px;border-radius:50%;background:#fff}
  .headline{position:absolute;top:66px;left:30px;right:10px;font-family:"Passion One",sans-serif;font-weight:700;font-size:34px;line-height:33px;
    text-transform:uppercase;text-shadow:2px 2px 0 rgba(0,0,0,.45)}

  .snap{position:absolute;background:#fff;padding:6px;box-shadow:0 3px 8px rgba(0,0,0,.3)}
  .snap__img{width:100%;height:100%}
  .snap--care{left:56px;top:338px;width:186px;height:146px;transform:rotate(13deg)}
  .snap--care .snap__img{background:linear-gradient(135deg,#e9eef2,#b7c7d4 50%,#8c4a5a)}
  .snap--beach{left:40px;top:502px;width:196px;height:144px;transform:rotate(2deg)}
  .snap--beach .snap__img{background:linear-gradient(180deg,#7fb0e0 0%,#a9cbea 40%,#3f7e9c 55%,#d9c7a3 75%,#cdb48e 100%)}
  .snap--park{left:30px;top:660px;width:206px;height:124px;transform:rotate(16deg)}
  .snap--park .snap__img{background:linear-gradient(160deg,#a7c08a,#5f7f4e 50%,#8b7a62)}

  .badge{position:absolute;left:214px;top:752px;width:44px;height:32px;background:#fff;border-radius:4px;transform:rotate(16deg)}

  .contact{position:absolute;left:22px;bottom:16px;font-size:13px;line-height:22px}
  .contact div{display:flex;align-items:center;gap:7px}
  .contact svg{width:12px;height:12px}
</style>
</head>
<body>
<article class="flyer">
  <section class="flyer__main">
    <header class="brand">
      <span class="brand__dot"></span><span class="brand__name">Lumenfield Hub</span>
    </header>
    <div class="hero" role="img" aria-label="Photo: silhouette of a person in a wheelchair at sunset on a hilltop"></div>

    <h2 class="section-title">ABOUT US:</h2>
    <p class="section-body">The Lumenfield Hub is an QPVT registered company that specialises in providing comprehensive and personalised support services to individuals with disabilities. As a trusted QPVT service provider, the Lumenfield Hub offers a wide range of supports and assistance to help participants achieve their goals and lead fulfilling lives.</p>

    <h2 class="section-title">OUR SERVICES:</h2>
    <p class="section-body">Lumenfield Hub's vision is to empower and enrich the lives of QPVT participants by providing innovative and tailored support services that promote independence, choice, and inclusion in the community.</p>
    <ul class="services">
      <li><svg viewBox="0 0 12 12"><circle cx="6" cy="6" r="6" fill="#3e8a2a"/><path d="M3.2 6.2l1.9 1.9 3.7-4" stroke="#fff" stroke-width="1.5" fill="none"/></svg>Community Participation</li>
      <li><svg viewBox="0 0 12 12"><circle cx="6" cy="6" r="6" fill="#3e8a2a"/><path d="M3.2 6.2l1.9 1.9 3.7-4" stroke="#fff" stroke-width="1.5" fill="none"/></svg>Supported Independent Living</li>
      <li><svg viewBox="0 0 12 12"><circle cx="6" cy="6" r="6" fill="#3e8a2a"/><path d="M3.2 6.2l1.9 1.9 3.7-4" stroke="#fff" stroke-width="1.5" fill="none"/></svg>Assistance with Daily Living</li>
      <li><svg viewBox="0 0 12 12"><circle cx="6" cy="6" r="6" fill="#3e8a2a"/><path d="M3.2 6.2l1.9 1.9 3.7-4" stroke="#fff" stroke-width="1.5" fill="none"/></svg>Specialist Disability Accommodation</li>
      <li><svg viewBox="0 0 12 12"><circle cx="6" cy="6" r="6" fill="#3e8a2a"/><path d="M3.2 6.2l1.9 1.9 3.7-4" stroke="#fff" stroke-width="1.5" fill="none"/></svg>Supported Holidays</li>
      <li><svg viewBox="0 0 12 12"><circle cx="6" cy="6" r="6" fill="#3e8a2a"/><path d="M3.2 6.2l1.9 1.9 3.7-4" stroke="#fff" stroke-width="1.5" fill="none"/></svg>Support Coordination</li>
    </ul>

    <footer class="phone">
      <svg viewBox="0 0 24 30"><path d="M6 2c1.5-.8 2.5 0 3.2 1.6l1.6 4c.5 1.3 0 2.2-1 2.9l-1.6 1c.8 3 2.6 6 5 8.2l1.5-1.2c1-.7 2-.7 2.9.2l3 3c1 1.1.9 2.2-.3 3.2-2 1.8-4.6 2.4-7.4.3C6.8 21 3 14 3 8c0-2.6 1.2-4.9 3-6z" fill="#fff"/></svg>
      <span class="phone__number">0491570156</span>
    </footer>
  </section>

  <aside class="flyer__side">
    <span class="site">www.lumenfieldhub.com.au</span>
    <h1 class="headline">Personalised<br>support<br>service<br>providers to<br>individuals<br>with<br>disabilities</h1>

    <div class="snap snap--care"><div class="snap__img" role="img" aria-label="Photo: carer assisting a young person in a wheelchair indoors"></div></div>
    <div class="snap snap--beach"><div class="snap__img" role="img" aria-label="Photo: person in a wheelchair on a beach with arms outstretched"></div></div>
    <div class="snap snap--park"><div class="snap__img" role="img" aria-label="Photo: group of wheelchair users together in a park"></div></div>
    <div class="badge" role="img" aria-label="Registered provider badge"></div>

    <div class="contact">
      <div><svg viewBox="0 0 12 12"><path d="M6 0a4 4 0 0 1 4 4c0 3-4 8-4 8S2 7 2 4a4 4 0 0 1 4-4z" fill="#fff"/><circle cx="6" cy="4" r="1.5" fill="#6dbb3c"/></svg>Lumen Bay Victoria</div>
      <div><svg viewBox="0 0 12 12"><rect x="0.5" y="2" width="11" height="8" fill="#fff"/><path d="M0.5 2l5.5 4.5L11.5 2" stroke="#6dbb3c" fill="none"/></svg>info@lumenfieldhub.com.au</div>
    </div>
  </aside>
</article>
</body>
</html>
```